KestrelNet Business Cards

Create business cards for our exciting new software company. We provide cloud billing systems and provisioning software for campany that need monthly SaaS and Cloud Billing

Target Market(s)

Enterprise businesses, b2b, telecom carriers, software manufactures

Industry/Entity Type

Software

```html
<!DOCTYPE html>
<html lang="en">
<head>
<meta charset="utf-8">
<title>KestrelNet Business Cards</title>
<link href="https://fonts.googleapis.com/css2?family=Questrial&family=Open+Sans:wght@400;600&display=swap" rel="stylesheet">
<style>
  :root {
    --backdrop: #f2efe9;
    --card-rim: #7dcbe8;
    --card-face-top: #ffffff;
    --card-face-bottom: #eef0f1;
    --brand-blue: #2f5f8c;
    --ink-navy: #1f3557;
    --ink-grey: #7b8088;
    --accent-dot: #7dcbe8;
  }
  * { margin: 0; padding: 0; box-sizing: border-box; }
  html, body {
    width: 1200px;
    height: 900px;
    overflow: hidden;
    background: var(--backdrop);
  }
  .sheet {
    position: relative;
    width: 1200px;
    height: 900px;
  }
  .card {
    position: absolute;
    top: 220px;
    width: 420px;
    height: 242px;
  }
  .card--front { left: 132px; }
  .card--back { left: 646px; }
  .card__shape {
    position: absolute;
    inset: 0;
    overflow: visible;
  }
  .card__text {
    position: absolute;
    font-family: "Questrial", sans-serif;
  }

  /* front */
  .front-brand {
    right: 97px;
    top: 143px;
    text-align: right;
  }
  .front-brand__name {
    font-size: 38px;
    line-height: 1;
    color: var(--brand-blue);
    letter-spacing: 0.5px;
  }
  .front-brand__tagline {
    margin-top: 8px;
    font-size: 7.5px;
    line-height: 10px;
    letter-spacing: 1.2px;
    color: var(--ink-navy);
    text-transform: uppercase;
  }

  /* back */
  .back-brand {
    right: 114px;
    top: 70px;
    text-align: right;
  }
  .back-brand__name {
    font-size: 18px;
    line-height: 1;
    color: var(--ink-navy);
  }
  .back-brand__tagline {
    margin-top: 3px;
    font-size: 4px;
    line-height: 5px;
    letter-spacing: 0.6px;
    color: var(--ink-navy);
    text-transform: uppercase;
  }
  .back-person {
    right: 111px;
    top: 126px;
    text-align: right;
    color: var(--ink-navy);
  }
  .back-person__name {
    font-size: 21px;
    font-variant: small-caps;
    letter-spacing: 1.5px;
    line-height: 1;
  }
  .back-person__role {
    margin-top: 5px;
    font-size: 10px;
    letter-spacing: 1.6px;
    text-transform: uppercase;
  }
  .back-contact {
    left: 46px;
    top: 193px;
    font-family: "Open Sans", sans-serif;
    font-size: 11.5px;
    color: var(--ink-grey);
    white-space: nowrap;
  }
  .back-contact__sep { color: var(--accent-dot); margin: 0 3px; }
</style>
</head>
<body>
<main class="sheet">

  <svg width="0" height="0" style="position:absolute" aria-hidden="true">
    <defs>
      <linearGradient id="face-fill" gradientUnits="userSpaceOnUse" x1="0" y1="15" x2="0" y2="227">
        <stop offset="0" stop-color="#ffffff"/>
        <stop offset="1" stop-color="#eef0f1"/>
      </linearGradient>
      <clipPath id="rim-clip">
        <rect x="0" y="0" width="420" height="242"/>
      </clipPath>
      <clipPath id="face-clip">
        <rect x="0" y="0" width="420" height="227"/>
      </clipPath>
      <filter id="card-shadow" x="-10%" y="-10%" width="120%" height="130%">
        <feDropShadow dx="0" dy="3" stdDeviation="4" flood-color="#000" flood-opacity="0.15"/>
      </filter>
      <g id="cloud-rim" clip-path="url(#rim-clip)">
        <circle cx="62" cy="180" r="62"/>
        <circle cx="233" cy="125" r="125"/>
        <circle cx="358" cy="180" r="62"/>
        <rect x="62" y="150" width="296" height="92"/>
      </g>
      <g id="cloud-face" clip-path="url(#face-clip)">
        <circle cx="62" cy="180" r="47"/>
        <circle cx="233" cy="125" r="110"/>
        <circle cx="358" cy="180" r="47"/>
        <rect x="62" y="150" width="296" height="77"/>
      </g>
    </defs>
  </svg>

  <section class="card card--front" aria-label="Card front">
    <svg class="card__shape" viewBox="0 0 420 242" aria-hidden="true">
      <g filter="url(#card-shadow)"><use href="#cloud-rim" fill="#7dcbe8"/></g>
      <use href="#cloud-face" fill="url(#face-fill)"/>
    </svg>
    <div class="card__text front-brand">
      <div class="front-brand__name">KestrelNet</div>
      <div class="front-brand__tagline">Cloud billing and<br>operational support systems</div>
    </div>
  </section>

  <section class="card card--back" aria-label="Card back">
    <svg class="card__shape" viewBox="0 0 420 242" aria-hidden="true">
      <g filter="url(#card-shadow)"><use href="#cloud-rim" fill="#7dcbe8"/></g>
      <use href="#cloud-face" fill="url(#face-fill)"/>
    </svg>
    <div class="card__text back-brand">
      <div class="back-brand__name">KestrelNet</div>
      <div class="back-brand__tagline">Cloud billing and<br>operational support systems</div>
    </div>
    <div class="card__text back-person">
      <div class="back-person__name">Marcus Ellery</div>
      <div class="back-person__role">Managing Director</div>
    </div>
    <div class="card__text back-contact">ellery.marcus@kestrelnet.com<span class="back-contact__sep">•</span>+55 2 555 0148</div>
  </section>

</main>
</body>
</html>
```